Building company buisness cards

We are looking for a sharp modern new look for our business cards.We are a New Zealand based company that specialises in house and land packages.We have attached a photo of the current logo and would like to see if it can be improved somehow if needed.We are open to any colours but we have chosen Black and White at this stage. Feel free to change the font and make the logo smarter looking.Play with the colours and see what looks best.We want a card that looks so good know one will want to throw it away!

Target Market(s)

Building profesonals, home buyers

Industry/Entity Type

Building

Contact Information for Business Card

Garrick Thorne
0274392068
garrickt@homevista.co.nz

Font styles to use
Serif
Sans Serif

Colors

Designer to choose colors to be used in the design.

Requirements
Must have
• Just the logo on one side and details on the other
• Clean simple looking card
Nice to have
• Round corners and detail like raised or spot UV
• Something that stands out
Should not have
• To title needed, Director etc

```html
<!DOCTYPE html>
<html lang="en">
<head>
<meta charset="utf-8">
<title>HomeVista Business Cards</title>
<link rel="stylesheet" href="https://fonts.googleapis.com/css2?family=Playfair+Display:wght@700&family=EB+Garamond:wght@400;700&family=Roboto:wght@400&display=swap">
<style>
  :root {
    --navy: #1d2757;
    --orange: #ef9f24;
    --white: #ffffff;
    --backdrop: #e4e4e4;
  }
  * { box-sizing: border-box; margin: 0; padding: 0; }
  html, body {
    width: 1125px;
    height: 1200px;
    overflow: hidden;
    background: var(--backdrop);
  }
  .canvas {
    position: relative;
    width: 1125px;
    height: 1200px;
  }
  .card {
    position: absolute;
    left: 162px;
    width: 800px;
    height: 457px;
    border-radius: 24px;
    overflow: hidden;
  }
  .card--front { top: 106px; background: var(--white); }
  .card--back { top: 638px; background: var(--navy); }

  .front-waves {
    position: absolute;
    inset: 0;
    width: 800px;
    height: 457px;
  }
  .wave-navy { fill: var(--navy); }
  .wave-orange { fill: var(--orange); }
  .wave-highlight { fill: var(--white); }

  .brand {
    position: absolute;
    left: 68px;
    top: 72px;
    display: flex;
    align-items: center;
    gap: 18px;
  }
  .brand__name {
    font-family: "Playfair Display", serif;
    font-weight: 700;
    font-size: 70px;
    line-height: 1;
    color: var(--navy);
  }
  .brand__ring {
    width: 82px;
    height: 82px;
    border: 4px solid var(--orange);
    border-radius: 50%;
  }

  .contact {
    position: absolute;
    right: 50px;
    top: 272px;
    text-align: right;
    color: var(--white);
    font-family: "EB Garamond", serif;
  }
  .contact__name {
    font-weight: 700;
    font-size: 29px;
    letter-spacing: 0.5px;
    text-transform: uppercase;
    margin-bottom: 22px;
  }
  .contact__line {
    display: flex;
    justify-content: flex-end;
    align-items: center;
    gap: 10px;
    font-size: 18px;
    line-height: 26px;
  }
  .contact__icon { width: 17px; height: 17px; fill: var(--white); }

  .back-brand {
    position: absolute;
    left: 0;
    right: 0;
    top: 130px;
    display: flex;
    justify-content: center;
    align-items: center;
    gap: 22px;
  }
  .back-brand__ring {
    width: 110px;
    height: 110px;
    border: 5px solid var(--white);
    border-radius: 50%;
  }
  .back-brand__name {
    font-family: "Playfair Display", serif;
    font-weight: 700;
    font-size: 60px;
    color: var(--white);
  }
  .back-web {
    position: absolute;
    left: 0;
    right: 0;
    top: 390px;
    text-align: center;
    font-family: "Roboto", sans-serif;
    font-size: 19px;
    letter-spacing: 9px;
    color: var(--white);
  }
</style>
</head>
<body>
<main class="canvas">
  <section class="card card--front">
    <svg class="front-waves" viewBox="0 0 800 457" aria-hidden="true">
      <path class="wave-orange" d="M0,312 C80,355 200,395 318,348 C220,392 90,380 0,358 Z"/>
      <path class="wave-navy" d="M0,372 C90,410 200,420 300,385 C400,350 470,240 560,175 C640,115 740,120 800,155 L800,457 L0,457 Z"/>
      <path class="wave-highlight" d="M540,190 C630,135 730,130 800,172 L800,198 C740,152 640,150 540,190 Z"/>
    </svg>

    <div class="brand">
      <span class="brand__name">HomeVista</span>
      <span class="brand__ring"></span>
    </div>

    <div class="contact">
      <p class="contact__name">Garrick Thorne</p>
      <p class="contact__line">0274392068
        <svg class="contact__icon" viewBox="0 0 24 24" aria-hidden="true"><path d="M6.6 10.8a15.1 15.1 0 0 0 6.6 6.6l2.2-2.2a1 1 0 0 1 1-.25 11.4 11.4 0 0 0 3.6.57 1 1 0 0 1 1 1V20a1 1 0 0 1-1 1A17 17 0 0 1 3 4a1 1 0 0 1 1-1h3.5a1 1 0 0 1 1 1c0 1.25.2 2.45.57 3.57a1 1 0 0 1-.25 1z"/></svg>
      </p>
      <p class="contact__line">garrickt@homevista.co.nz
        <svg class="contact__icon" viewBox="0 0 24 24" aria-hidden="true"><path d="M2 5h20v14H2z M3.5 6.5 12 13l8.5-6.5" fill="none" stroke="#fff" stroke-width="2"/><path d="M2 5h20v14H2z"/><path d="M3 6l9 7 9-7" fill="none" stroke="#1d2757" stroke-width="1.6"/></svg>
      </p>
      <p class="contact__line">www.homevista.co.nz
        <svg class="contact__icon" viewBox="0 0 24 24" aria-hidden="true"><circle cx="12" cy="12" r="10"/><path d="M12 2v20M2 12h20M12 2a15 15 0 0 1 0 20M12 2a15 15 0 0 0 0 20" fill="none" stroke="#1d2757" stroke-width="1.4"/></svg>
      </p>
    </div>
  </section>

  <section class="card card--back">
    <div class="back-brand">
      <span class="back-brand__ring"></span>
      <span class="back-brand__name">HomeVista</span>
    </div>
    <p class="back-web">www.HomeVista.co.nz</p>
  </section>
</main>
</body>
</html>
```